political campaign lawn sign - Governor's Council in Massachuesetts

We are looking for a political lawn sign. We are running a campaign for Governor's Council in Massachusetts. This sign will be on the lawn of homes and businesses so people driving by will see it. It needs to be simple and bold. The last name is long so maybe it could say vote for Carl and then Malbonske will be big a bold on the next line??
We need it to say:
Vote for Carlton Malbonske
Governor's Council.

Target Market(s)

local residents

Industry/Entity Type

Politcal Campaign

Font styles to use
Sans Serif
Other font styles liked:
• not sure what font but a modern looking one such as Helvetica, Arial, Sans Seri, sharp sans..

Colors
0054AA
0677BA
7BADD7
CADEEF
E8F1F8
00AB8E
00BBA5
67D7C9
C6EFE9
E9F9F6
FFF300
FFF600
FEFA6F
FFFEC7
FFFEE8

Requirements
Must have
• My name written out with a Capital D and R but lower case for every other letter so its Carl Malbonske
Nice to have
• modern font , the Colors of the lawn sign should have Blue, Yellow and White something bold that will stand out
Should not have
• any maps of Massachusetts

```html
<!DOCTYPE html>
<html lang="en">
<head>
<meta charset="utf-8">
<title>Vote for Carl Malbonske – Governor's Council</title>
<link rel="stylesheet" href="https://fonts.googleapis.com/css2?family=Anton&family=Montserrat:wght@700;800&display=swap">
<style>
  :root {
    --campaign-blue: #0054AA;
    --sign-white: #FFFFFF;
  }
  html, body {
    margin: 0;
    padding: 0;
    width: 1200px;
    height: 900px;
    overflow: hidden;
    background: var(--campaign-blue);
  }
  .lawn-sign {
    display: block;
    width: 1200px;
    height: 900px;
  }
  .sign-field { fill: var(--campaign-blue); }
  .diagonal-band, .office-band { fill: var(--sign-white); }
  .vote-for {
    font-family: "Montserrat", sans-serif;
    font-weight: 700;
    font-size: 140px;
    fill: var(--campaign-blue);
  }
  .first-name {
    font-family: "Montserrat", sans-serif;
    font-weight: 800;
    font-size: 250px;
    fill: var(--sign-white);
  }
  .last-name {
    font-family: "Anton", sans-serif;
    font-size: 262px;
    fill: var(--sign-white);
  }
  .office-title {
    font-family: "Montserrat", sans-serif;
    font-weight: 700;
    font-size: 88px;
    fill: var(--campaign-blue);
  }
</style>
</head>
<body>
<svg class="lawn-sign" viewBox="0 0 1200 900" xmlns="http://www.w3.org/2000/svg" aria-label="Vote for Carl Malbonske, Governor's Council">
  <rect class="sign-field" x="0" y="0" width="1200" height="900"/>
  <polygon class="diagonal-band" points="0,201 526,0 1040,0 0,399"/>

  <text class="vote-for" transform="translate(85,315) rotate(-21)" x="0" y="0" textLength="590" lengthAdjust="spacingAndGlyphs">Vote for</text>

  <text class="first-name" x="1165" y="407" text-anchor="end">Carl</text>

  <text class="last-name" x="22" y="670" textLength="1156" lengthAdjust="spacingAndGlyphs">MALBONSKE</text>

  <rect class="office-band" x="0" y="705" width="1200" height="106"/>
  <text class="office-title" x="66" y="788" textLength="1067" lengthAdjust="spacingAndGlyphs">GOVERNOR'S COUNCIL</text>
</svg>
</body>
</html>
```